Flyer für ein Küchenfachgeschäft
Zielgruppe
Wir sind ein Küchenfachgeschäft und würden hierfür gerne einen Flyer für Hochwertige und Qualitative Küchen einen Flyer erstellen lassen.
Aufgabenstellung
US gefaltet Format, Hochwertig und ansprechend. Wir sind Berater, Planer und Ausführer. 35 Jahre Erfahrung

```html
<!DOCTYPE html>
<html lang="de">
<head>
<meta charset="UTF-8">
<title>Flyer Küchenfachgeschäft</title>
<link rel="stylesheet" href="https://fonts.googleapis.com/css2?family=Josefin+Sans:wght@300&family=Montserrat:wght@600&family=Open+Sans:wght@400;700&display=swap">
<style>
  :root {
    --page-bg: #e6e6e8;
    --panel-dark: #2e3132;
    --text-light: #f4f4f4;
    --text-muted: #d9d9d9;
    --photo-top: #a9aaa9;
    --photo-mid: #6e6a63;
    --photo-low: #2b2a28;
  }
  * { box-sizing: border-box; margin: 0; padding: 0; }
  html, body {
    width: 1200px; height: 900px; overflow: hidden;
    background: var(--page-bg);
    font-family: "Open Sans", Arial, sans-serif;
  }
  .flyer {
    position: absolute; left: 260px; top: 80px;
    width: 680px; height: 740px;
    display: flex;
  }
  .panel { position: relative; width: 340px; height: 740px; overflow: hidden; }

  .cover-photo {
    position: absolute; inset: 0;
    background:
      linear-gradient(180deg, var(--photo-top) 0%, #8d8c89 28%, #c9b8a2 42%, var(--photo-mid) 55%, var(--photo-low) 78%, #7d7b78 100%);
  }
  .cover-kicker {
    position: absolute; right: 12px; top: 100px;
    font-family: "Josefin Sans", Arial, sans-serif; font-weight: 300;
    font-size: 22px; letter-spacing: 1px; font-variant: small-caps;
    color: var(--text-light);
  }
  .cover-name {
    position: absolute; right: 12px; top: 138px;
    font-family: "Montserrat", Arial, sans-serif; font-weight: 600;
    font-size: 38px; color: #ffffff;
  }
  .address {
    position: absolute; left: 18px; top: 685px;
    font-family: "Josefin Sans", Arial, sans-serif; font-weight: 300;
    font-size: 19px; line-height: 1.05; letter-spacing: 1px;
    font-variant: small-caps; color: var(--text-light);
  }

  .panel-info { background: var(--panel-dark); }
  .info-photo {
    position: absolute; border-radius: 50%;
  }
  .info-photo--oven {
    left: -75px; top: 45px; width: 190px; height: 190px;
    background: radial-gradient(circle at 60% 45%, #4a4c4d 0%, #1d1e1f 45%, #cfd0cf 75%, #e9e9e9 100%);
  }
  .info-photo--tap {
    left: 140px; top: 470px; width: 185px; height: 185px;
    background: radial-gradient(circle at 45% 40%, #f3f3f3 0%, #dcdcdc 55%, #b9b9b9 85%, #8e8e8e 100%);
  }
  .info-text {
    position: absolute; right: 14px;
    font-size: 12.5px; line-height: 1.55; text-align: right;
    color: var(--text-muted);
  }
  .info-welcome { top: 62px; width: 185px; }
  .info-dive { top: 248px; width: 250px; }
  .promise {
    position: absolute; left: 18px; top: 398px;
    font-size: 12.5px; line-height: 1.55; font-weight: 700;
    color: var(--text-light);
  }
</style>
</head>
<body>
  <main class="flyer">
    <section class="panel panel-cover">
      <div class="cover-photo" role="img" aria-label="Foto einer modernen dunklen Küche mit Esstisch und Hängeschränken"></div>
      <p class="cover-kicker">Küchenfachgeschäft</p>
      <h1 class="cover-name">Name</h1>
      <p class="address">Adresse<br>Strassestrasse 234</p>
    </section>

    <section class="panel panel-info">
      <div class="info-photo info-photo--oven" role="img" aria-label="Foto von Einbaubacköfen in einer Küchenzeile"></div>
      <p class="info-text info-welcome">Willkommen bei [Name des Küchengeschäfts] - Ihrer Quelle für hochwertige Küchenlösungen, die Ihre kulinarischen Träume wahr werden lassen.</p>
      <p class="info-text info-dive">Tauchen Sie ein in eine Welt voller Eleganz, Funktionalität und zeitlosem Design und lassen Sie uns Ihnen helfen, die Küche Ihrer Träume zu gestalten.</p>
      <p class="promise">Unser Versprechen an Sie:<br>Exzellenz in jeder<br>Facette</p>
      <div class="info-photo info-photo--tap" role="img" aria-label="Foto einer schwarzen Küchenarmatur vor Marmorwand"></div>
      <p class="address">Adresse:<br>Strassestrasse 234</p>
    </section>
  </main>
</body>
</html>
```